Business Card Design Project 4 Construction Business

I am after a creative, but sleek and simple/ clean business card design. This design will form the basis of future items and might include a logo or simply a creative way to lay out the text of my company name 'keldmoor builds'
I like the simplicity of black and white however I would also be happy to see a splash of colour introduced somehow to give the text some interest and make it stand out.
I would like a double sided card.
I am young (ish!) and professional, offering construction and project management services, what I don't want is the traditional builders type card featuring a cheesy hammer/ saw image etc.
As the company name, keldmoor builds, suggests, we focus on working closely and collaboratively together, in synergy with all stakeholders involved in the projects that we undertake
Industry/Entity Type
Construction

```html
<!DOCTYPE html>
<html lang="en">
<head>
<meta charset="utf-8">
<title>keldmoor builds – business card</title>
<link href="https://fonts.googleapis.com/css2?family=Open+Sans:wght@400;600&display=swap" rel="stylesheet">
<style>
  :root {
    --stage: #d9dadb;
    --card-black: #151515;
    --card-white: #f1f1f1;
    --accent-red: #d6343a;
    --ink-dark: #2b2b2b;
    --ink-grey: #a9a9a9;
    --ink-light: #e8e6df;
  }
  * { margin: 0; padding: 0; box-sizing: border-box; }
  html, body {
    width: 1200px; height: 900px; overflow: hidden;
    background: var(--stage);
    font-family: "Open Sans", Arial, sans-serif;
  }
  .stage {
    width: 1200px; height: 900px;
    display: flex; align-items: center; justify-content: center; gap: 44px;
  }
  .card {
    width: 530px; height: 303px; position: relative; overflow: hidden;
    box-shadow: 0 10px 28px rgba(0,0,0,0.22);
  }

  /* front side */
  .card-front { background: var(--card-white); }
  .front-band {
    position: absolute; left: 0; top: 0; width: 100%; height: 108px;
    background: var(--card-black);
  }
  .front-wordmark {
    position: absolute; right: 28px; top: 118px;
    font-size: 30px; font-weight: 400; letter-spacing: 0.5px;
    color: var(--ink-grey);
  }
  .holder { position: absolute; left: 34px; bottom: 40px; }
  .holder-name {
    font-size: 19px; font-weight: 400; letter-spacing: 1.5px;
    color: var(--ink-dark); text-transform: uppercase;
  }
  .holder-role {
    font-size: 11px; font-weight: 600; letter-spacing: 1.5px;
    color: var(--accent-red); text-transform: uppercase;
  }
  .contact-list {
    position: absolute; right: 28px; top: 170px;
    list-style: none; font-size: 11.5px; color: var(--ink-dark);
  }
  .contact-list li { display: flex; align-items: center; gap: 9px; height: 19px; }
  .contact-icon { width: 11px; height: 11px; fill: var(--accent-red); flex: none; }

  /* back side */
  .card-back {
    background: var(--card-black);
    display: flex; align-items: center; justify-content: center;
  }
  .back-wordmark {
    font-size: 36px; font-weight: 400; letter-spacing: 0.5px;
    color: var(--accent-red);
  }
</style>
</head>
<body>
<main class="stage">
  <section class="card card-front" aria-label="Card front">
    <div class="front-band"></div>
    <p class="front-wordmark">keldmoor builds</p>
    <div class="holder">
      <p class="holder-name">Tomas Hale</p>
      <p class="holder-role">Director</p>
    </div>
    <ul class="contact-list">
      <li>
        <svg class="contact-icon" viewBox="0 0 12 12" aria-hidden="true"><path d="M2.4 0.6 4.4 2.8 3.3 4.3C4 5.9 6 7.9 7.7 8.7L9.2 7.6 11.4 9.6 10.2 11.4C5.2 11 1 6.8 0.6 1.8Z"/></svg>
        <span>0400 555 218</span>
      </li>
      <li>
        <svg class="contact-icon" viewBox="0 0 12 12" aria-hidden="true"><path d="M0.5 2.5H11.5V3.3L6 6.8 0.5 3.3ZM0.5 4.5 6 8 11.5 4.5V9.8H0.5Z"/></svg>
        <span>tomas@keldmoorbuilds.com.au</span>
      </li>
      <li>
        <svg class="contact-icon" viewBox="0 0 12 12" aria-hidden="true"><path d="M6 0.8 11.4 5.6H9.8V11.2H7.2V7.8H4.8V11.2H2.2V5.6H0.6Z"/></svg>
        <span>14 Ashgrove St Lindale NSW 2071</span>
      </li>
      <li>
        <svg class="contact-icon" viewBox="0 0 12 12" aria-hidden="true"><path d="M4.8 0.6A4.2 4.2 0 1 1 4.8 9 4.2 4.2 0 1 1 4.8 0.6ZM4.8 2.2A2.6 2.6 0 1 0 4.8 7.4 2.6 2.6 0 1 0 4.8 2.2ZM7.6 8.2 8.8 7 11.6 9.8 10.4 11Z"/></svg>
        <span>www.keldmoorbuilds.com.au</span>
      </li>
    </ul>
  </section>

  <section class="card card-back" aria-label="Card back">
    <p class="back-wordmark">keldmoor builds</p>
  </section>
</main>
</body>
</html>
```